Larkfield Homecare - Website

MUST HAVE EXPERIENCE DESIGNING WEBSITES HEALTH CARE IN GENERAL AND/OR HOME NURSING SERVICES.

Details attached.

Number of Pages Required

1 page

Requirements
Must have
• Warm feel
caregivers

Color similar to the logo...

```html
<!DOCTYPE html>
<html lang="en">
<head>
<meta charset="utf-8">
<title>Larkfield Homecare</title>
<link href="https://fonts.googleapis.com/css2?family=IBM+Plex+Sans:wght@400;500;600&family=Poppins:wght@500;600;700&display=swap" rel="stylesheet">
<style>
:root{
  --teal:#1a8d96;
  --orange:#ee6b12;
  --ink:#1d1d1d;
  --text:#3a3a3a;
  --muted:#5a5a5a;
  --paper:#ffffff;
  --footer:#f4f1f1;
  --line:#dddddd;
}
*{box-sizing:border-box;margin:0;padding:0}
html,body{width:1200px;height:3648px;overflow:hidden;background:var(--paper)}
body{position:relative;font-family:"IBM Plex Sans",Arial,sans-serif;color:var(--text)}
.abs{position:absolute}
.head-font{font-family:"Poppins",Arial,sans-serif}
.btn{position:absolute;display:flex;align-items:center;justify-content:center;background:var(--orange);color:#fff;font-family:"Poppins",Arial,sans-serif;font-weight:600;text-transform:uppercase;letter-spacing:.3px}

/* header */
.brand{position:absolute;display:flex;align-items:center;gap:10px;font-family:"Poppins",Arial,sans-serif;font-weight:600;color:var(--teal)}
.brand-dot{border-radius:50%;background:var(--orange)}
.service-btn{position:absolute;left:686px;top:28px;width:157px;height:42px;background:var(--teal);color:#fff;font:600 14px "Poppins",Arial,sans-serif;display:flex;align-items:center;justify-content:center;letter-spacing:.3px}
.call{position:absolute;left:870px;top:28px;display:flex;align-items:center}
.call-divider{width:1px;height:40px;background:#999;margin:0 15px 0 14px}
.call-label{font-size:14px;color:var(--ink);line-height:16px}
.call-number{font:500 21px "IBM Plex Sans",Arial,sans-serif;color:var(--ink);line-height:26px}
.nav{position:absolute;top:99px;left:0;width:1200px;height:20px;font-size:14px;color:var(--ink)}
.nav a{position:absolute;color:var(--ink);text-decoration:none}
.nav a.active{color:var(--orange);font-weight:500;border-bottom:2px solid var(--orange);padding-bottom:1px}

/* hero */
.hero-photo{position:absolute;left:0;top:135px;width:1200px;height:534px;background:linear-gradient(100deg,#c9c4bb 0%,#ddd7cc 35%,#eee9df 60%,#e6e3d7 100%)}
.hero-card{position:absolute;left:734px;top:238px;width:347px;height:234px;background:rgba(255,255,255,.92);padding:24px 0 0 34px}
.hero-card h1{font:700 34px/40px "Poppins",Arial,sans-serif;color:var(--teal)}
.hero-card p{font-size:24px;line-height:32px;color:var(--ink);margin-top:8px}
.dots{position:absolute;top:624px;left:553px;display:flex;gap:13px}
.dots span{width:9px;height:9px;border-radius:50%;background:#fff}
.dots span.on{background:none;border:2px solid var(--orange);width:11px;height:11px;margin-top:-1px}

.section-title{position:absolute;left:0;width:1200px;text-align:center;font:700 21px "Poppins",Arial,sans-serif;color:var(--teal)}
.rule{position:absolute;left:581px;width:38px;height:2px;background:var(--teal)}

/* services */
.svc-card{position:absolute;top:788px;width:461px;height:437px;border:3px solid #e5e5e5;border-top:none;background:#fff}
.svc-photo{height:280px;margin:0 -3px}
.svc-card h3{font:600 17px "Poppins",Arial,sans-serif;color:var(--ink);margin:22px 0 0 32px}
.svc-card p{font-size:13px;line-height:17.5px;color:var(--text);margin:20px 0 0 33px;width:360px}
.svc-card .btn{left:36px;top:414px;width:90px;height:32px;font-size:11px}

/* welcome */
.welcome{position:absolute;left:0;top:1291px;width:1200px;height:515px;background:linear-gradient(90deg,#f3e9e4 0%,#f1e4dd 40%,#e8cdbf 70%,#e3c0ae 100%)}
.welcome-photo{position:absolute;left:480px;top:0;width:720px;height:515px;background:radial-gradient(ellipse at 45% 50%,#efe2d8 0%,#e9d2c4 50%,rgba(227,192,174,0) 80%)}
.welcome small{position:absolute;left:130px;top:35px;font:700 22px "Poppins",Arial,sans-serif;color:var(--teal)}
.welcome h2{position:absolute;left:130px;top:63px;font:700 30px "Poppins",Arial,sans-serif;color:var(--teal)}
.welcome .wrule{position:absolute;left:130px;top:120px;width:38px;height:2px;background:var(--teal)}
.welcome p{position:absolute;left:131px;width:340px;font-size:14.5px;line-height:21.6px;color:var(--ink)}
.welcome .btn{left:130px;top:432px;width:91px;height:32px;font-size:11px}

/* news */
.news{position:absolute;left:0;top:1806px;width:1200px;height:536px;background:var(--teal)}
.news .section-title{top:40px;color:#fff}
.news .rule{top:76px;background:#fff}
.news-card{position:absolute;top:121px;width:297px;height:371px;background:#fff}
.news-photo{height:187px}
.news-card h4{font:600 13px/20px "Poppins",Arial,sans-serif;color:var(--ink);text-transform:uppercase;margin:26px 0 0 22px}
.news-card p{font-size:12px;line-height:16px;color:var(--muted);margin:10px 0 0 23px;width:250px}
.news-card .btn{left:26px;top:321px;width:90px;height:31px;font-size:11px}

/* testimonials */
.testi{position:absolute;left:0;top:2342px;width:1200px;height:470px;background:linear-gradient(120deg,#f6f2ef 0%,#ece4dd 30%,#f5f1ee 60%,#ede6e1 100%)}
.testi .section-title{top:40px}
.testi .rule{top:82px}
.quote-card{position:absolute;top:127px;width:462px;height:291px;background:rgba(255,255,255,.82)}
.quote-mark{position:absolute;left:32px;top:22px;font:700 38px/1 "Poppins",Arial,sans-serif;color:var(--orange)}
.quote-card p{position:absolute;left:55px;top:50px;width:385px;font-size:17px;line-height:26.5px;color:var(--text)}
.quote-by{position:absolute;left:60px;top:233px;display:flex;align-items:center;font-size:12px;color:var(--muted)}
.quote-by i{display:block;width:30px;height:1px;background:var(--teal);margin-right:12px}
.quote-by b{color:var(--teal);font-weight:600;margin-right:3px}
.arrow{position:absolute;top:2594px}

/* join */
.join-photo{position:absolute;left:493px;top:2853px;width:577px;height:411px;background:linear-gradient(110deg,#cdbba2 0%,#b89a7a 45%,#8e6f55 75%,#6d5440 100%)}
.join-card{position:absolute;left:130px;top:2913px;width:437px;height:304px;background:#fff;box-shadow:0 4px 18px rgba(0,0,0,.08)}
.join-card h2{position:absolute;left:48px;top:40px;font:700 29px "Poppins",Arial,sans-serif;color:var(--teal)}
.join-card p{position:absolute;left:48px;top:100px;width:360px;font-size:17px;line-height:26.5px;color:var(--text)}
.join-card .btn{left:53px;top:224px;width:117px;height:40px;font-size:14px}

/* footer */
.footer{position:absolute;left:0;top:3308px;width:1200px;height:340px;background:var(--footer)}
.col-title{position:absolute;top:42px;font:600 13px "Poppins",Arial,sans-serif;color:var(--ink);letter-spacing:.3px}
.menu-list{position:absolute;left:450px;top:75px;list-style:none;font-size:12px;line-height:19.8px;color:var(--ink);text-transform:uppercase}
.f-row{position:absolute;display:flex;align-items:flex-start;font-size:12px;line-height:15.5px;color:var(--ink)}
.f-icon{width:22px;height:22px;border-radius:50%;background:var(--teal);margin-right:10px;flex:none;display:flex;align-items:center;justify-content:center}
.f-rule{position:absolute;left:130px;top:290px;width:940px;height:1px;background:var(--line)}
.copy{position:absolute;left:0;top:306px;width:1200px;text-align:center;font-size:10px;color:var(--ink)}
</style>
</head>
<body>

<header>
  <div class="brand" style="left:130px;top:34px;font-size:24px">
    <span class="brand-dot" style="width:36px;height:36px"></span>
    <span>Larkfield Homecare</span>
  </div>
  <div class="service-btn">SERVICE REQUEST</div>
  <div class="call">
    <svg width="36" height="36" viewBox="0 0 36 36" aria-hidden="true">
      <path d="M10 8c2-1 3 0 4 2l2 4c1 2 0 3-1 4l-1 1c1 3 4 6 7 7l1-1c1-1 2-2 4-1l4 2c2 1 3 2 2 4-1 3-4 4-7 3C17 31 8 22 6 14c-1-3 1-5 4-6z" fill="none" stroke="var(--teal)" stroke-width="2"/>
      <path d="M21 6a10 10 0 0 1 9 9M21 11a5 5 0 0 1 4 4" fill="none" stroke="var(--teal)" stroke-width="2"/>
    </svg>
    <span class="call-divider"></span>
    <div>
      <div class="call-label">CALL US</div>
      <div class="call-number">555.014.2277</div>
    </div>
  </div>
  <nav class="nav">
    <a class="active" style="left:133px">HOME</a>
    <a style="left:208px">ABOUT US</a>
    <a style="left:311px">SERVICES</a>
    <a style="left:414px">JOIN OUR TEAM</a>
    <a style="left:562px">NEWS</a>
    <a style="left:643px">CORONAVIRUS UPDATE</a>
    <a style="left:845px">TESTIMONIALS</a>
    <a style="left:987px">CONTACT US</a>
  </nav>
</header>

<section>
  <div class="hero-photo" role="img" aria-label="Nurse holding hands with an elderly woman on a sofa in a bright living room"></div>
  <div class="hero-card">
    <h1>HOME NURSING</h1>
    <p>Highly qualified and<br>experienced nurses.</p>
  </div>
  <div class="btn" style="left:771px;top:398px;width:117px;height:43px;font-size:14px">Read More</div>
  <div class="dots"><span></span><span></span><span class="on"></span><span></span><span></span></div>
</section>

<section>
  <div class="section-title" style="top:704px">OUR SERVICES</div>
  <div class="rule" style="top:746px"></div>

  <article class="svc-card" style="left:130px">
    <div class="svc-photo" role="img" aria-label="Nurse with a clipboard talking to an elderly woman" style="background:linear-gradient(90deg,#e6e8ea,#d7dde3 50%,#c9b4ad)"></div>
    <h3>Home Nursing</h3>
    <p>Looking for care, custodial care, Urinary catheterization care, Wound care, Injections, IV infusions, Vaccination or other nursing assistance?</p>
    <div class="btn">Read More</div>
  </article>

  <article class="svc-card" style="left:609px">
    <div class="svc-photo" role="img" aria-label="Mother cuddling her smiling toddler" style="background:linear-gradient(90deg,#d8d2cc,#b08a72 55%,#5b4033)"></div>
    <h3>New Born Baby And Mother Care At Home</h3>
    <p>Worried about your newborn’s needs? Facing issues in coping up with the initial challenges of feeding infant child and post-operative recovery?</p>
    <div class="btn">Read More</div>
  </article>
</section>

<section class="welcome">
  <div class="welcome-photo" role="img" aria-label="Mother lifting her laughing baby in the air"></div>
  <small>Welcome to</small>
  <h2>Larkfield Homecare</h2>
  <div class="wrule"></div>
  <p style="top:152px">Everyone should be free to experience joy and optimism in their lives, regardless of their age or condition. Larkfield Homecare provides a range of services that are tailored to meet the patient’s needs, helping them to maintain their independence and live happy and fulfilling lives.</p>
  <p style="top:302px;width:345px">Larkfield Homecare deliver comprehensive care to new born baby and mother, and elderly in the comfort of their own homes, we ensure that the needs of our clients and their families are at the heart of everything they do.</p>
  <div class="btn">Read More</div>
</section>

<section class="news">
  <div class="section-title">LATEST NEWS</div>
  <div class="rule"></div>

  <article class="news-card" style="left:129px">
    <div class="news-photo" role="img" aria-label="Newborn baby resting on its mother" style="background:linear-gradient(90deg,#b47e60,#e5ded9 55%,#c7a793)"></div>
    <h4>Lorem ipsum dolor sit amet<br>consectetur adipiscing</h4>
    <p>Sed ut perspiciatis unde omnis iste natus error sit voluptatem accusantium dolo remque laudantium.</p>
    <div class="btn">Read More</div>
  </article>

  <article class="news-card" style="left:452px">
    <div class="news-photo" role="img" aria-label="Carer embracing a smiling elderly woman" style="background:linear-gradient(90deg,#8d7a6c,#cfc2b6 45%,#e4d6c7)"></div>
    <h4>Lorem ipsum dolor sit amet<br>consectetur adipiscing</h4>
    <p>Sed ut perspiciatis unde omnis iste natus error sit voluptatem accusantium dolo remque laudantium.</p>
    <div class="btn">Read More</div>
  </article>

  <article class="news-card" style="left:772px">
    <div class="news-photo" role="img" aria-label="Nurse sitting beside an elderly woman at home" style="background:linear-gradient(90deg,#b7c0b0,#3f8fa3 45%,#d9d3c6)"></div>
    <h4>Lorem ipsum dolor sit amet<br>consectetur adipiscing</h4>
    <p>Sed ut perspiciatis unde omnis iste natus error sit voluptatem accusantium dolo remque laudantium.</p>
    <div class="btn">Read More</div>
  </article>
</section>

<section class="testi">
  <div class="section-title">TESTIMONIALS</div>
  <div class="rule"></div>

  <blockquote class="quote-card" style="left:129px">
    <span class="quote-mark">“</span>
    <p>On the other hand, we denounce with right eous indignation and dislike men who are so beguiled and demoralized by the charms of pleasure of the moment, so blinded by desire, that they cannot foresee the pain and trouble that are bound to ensue.</p>
    <div class="quote-by"><i></i><b>MARGARET</b>, Verona</div>
  </blockquote>

  <blockquote class="quote-card" style="left:608px">
    <span class="quote-mark">“</span>
    <p>On the other hand, we denounce with right eous indignation and dislike men who are so beguiled and demoralized by the charms of pleasure of the moment, so blinded by desire, that they cannot foresee the pain and trouble that are bound to ensue.</p>
    <div class="quote-by"><i></i><b>MARGARET</b>, Verona</div>
  </blockquote>
</section>
<svg class="arrow" style="left:68px" width="20" height="28" viewBox="0 0 20 28" aria-hidden="true"><path d="M15 3 5 14l10 11" fill="none" stroke="#555" stroke-width="2.5"/></svg>
<svg class="arrow" style="left:1105px" width="20" height="28" viewBox="0 0 20 28" aria-hidden="true"><path d="M5 3l10 11L5 25" fill="none" stroke="#555" stroke-width="2.5"/></svg>

<section>
  <div class="join-photo" role="img" aria-label="Young carer with her hand on the shoulder of a smiling elderly woman"></div>
  <div class="join-card">
    <h2>Join our Team</h2>
    <p>On the other hand, we denounce with right eous indignation and dislike men who are so beguiled and demoralized by the charms of pleasure of the moment,</p>
    <div class="btn">Read More</div>
  </div>
</section>

<footer class="footer">
  <div class="brand" style="left:130px;top:100px;font-size:26px">
    <span class="brand-dot" style="width:44px;height:44px"></span>
    <span>Larkfield Homecare</span>
  </div>

  <div class="col-title" style="left:450px">MENU</div>
  <ul class="menu-list">
    <li>Home</li><li>About Us</li><li>Services</li><li>Join Our Team</li><li>News</li><li>Coronavirus Update</li><li>Testimonials</li><li>Contact Us</li>
  </ul>

  <div class="col-title" style="left:667px">CONTACT US</div>
  <div class="f-row" style="left:667px;top:100px">
    <span class="f-icon"><svg width="10" height="12" viewBox="0 0 10 12"><path d="M5 0a4 4 0 0 1 4 4c0 3-4 8-4 8S1 7 1 4a4 4 0 0 1 4-4z" fill="#fff"/><circle cx="5" cy="4" r="1.5" fill="var(--teal)"/></svg></span>
    <span>2190 Alder Lane<br>Brookvale, CA 90412</span>
  </div>
  <div class="f-row" style="left:667px;top:152px">
    <span class="f-icon"><svg width="11" height="11" viewBox="0 0 11 11"><path d="M2 1c1 0 1 0 2 2L3 4c1 2 2 3 4 4l1-1c2 1 2 1 2 2s-1 2-2 2C4 11 0 7 0 3c0-1 1-2 2-2z" fill="#fff"/></svg></span>
    <span>Call Us<br>555.014.2277</span>
  </div>
  <div class="f-row" style="left:667px;top:202px">
    <span class="f-icon"><svg width="11" height="9" viewBox="0 0 11 9"><rect x="0" y="0" width="11" height="9" rx="1" fill="#fff"/><path d="M0 1l5.5 4L11 1" fill="none" stroke="var(--teal)" stroke-width="1.2"/></svg></span>
    <span>E mail Us<br>info@LarkfieldHomecare.com</span>
  </div>

  <div class="col-title" style="left:931px">FOLLOW US</div>
  <div class="f-row" style="left:931px;top:100px"><span class="f-icon"></span><span>Like us on<br>CIRCLEPAGE</span></div>
  <div class="f-row" style="left:931px;top:150px"><span class="f-icon"></span><span>Follow us on<br>CHIRPLINE</span></div>
  <div class="f-row" style="left:931px;top:201px"><span class="f-icon"></span><span>Follow us on<br>WORKNET</span></div>

  <div class="f-rule"></div>
  <div class="copy">Copyright © 2021 All Rights Reserved</div>
</footer>

</body>
</html>
```